Box Design for Concrete Mixer Truck Parts

Overview:
KVGEARS, a trusted supplier of concrete mixer, heavy-duty truck, and batch plant parts, is seeking a creative and professional packaging design for boxes that will contain concrete mixer truck parts. The design should reflect our brand identity while ensuring practicality and visual appeal.

Design Requirements:

Branding: The box must prominently feature the KVGEARS logo (attached).
Part Number Area: Include a designated space where part number stickers can be applied.
Color Scheme: The design should incorporate red as a primary color and may include up to three colors in total.
Style: The box should have a slick, modern, and creative design that aligns with our industry and brand.
Functionality: The design should be visually appealing while maintaining a professional and industrial feel, suitable for heavy-duty truck parts packaging.

We've included the box template and an example of a box using this template to help with orientation.

```html
<!DOCTYPE html>
<html lang="en">
<head>
<meta charset="utf-8">
<title>KVGEARS – Air System Components Box Dieline</title>
<link href="https://fonts.googleapis.com/css2?family=Exo+2:wght@700;900&family=Oswald:wght@300;400&family=Arimo:wght@400&display=swap" rel="stylesheet">
<style>
  :root{
    --brand-red:#ed1c24;
    --deep-red:#8b0a0e;
    --steel:#8a8b8f;
    --charcoal:#4a4a4c;
    --paper:#ffffff;
  }
  html,body{margin:0;padding:0;overflow:hidden;background:var(--paper);}
  .dieline{display:block;width:1200px;height:857px;}
  .red{fill:var(--brand-red);}
  .white{fill:var(--paper);}
  .deep{fill:var(--deep-red);}
  .steel{fill:var(--steel);}
  .fold{stroke:var(--paper);stroke-width:.8;fill:none;}
  .brand-name{font-family:"Exo 2",sans-serif;font-weight:900;fill:var(--charcoal);letter-spacing:.5px;}
  .brand-tag{font-family:"Oswald",sans-serif;font-weight:300;fill:var(--charcoal);}
  .product-title{font-family:"Exo 2",sans-serif;font-weight:700;fill:var(--brand-red);}
  .genuine{font-family:"Arimo",sans-serif;fill:var(--paper);}
  .brand-rule{stroke:var(--charcoal);stroke-width:1.4;}
  .mark-square{fill:none;stroke:var(--paper);stroke-width:2.4;}
  .mark-square-red{fill:none;stroke:var(--brand-red);stroke-width:2;}
</style>
</head>
<body>
<svg class="dieline" viewBox="0 0 1200 857" xmlns="http://www.w3.org/2000/svg">
  <defs>
    <linearGradient id="deepFade" x1="0" y1="0" x2="1" y2="1">
      <stop offset="0" stop-color="#8b0a0e"/><stop offset="1" stop-color="#ed1c24" stop-opacity="0"/>
    </linearGradient>
    <linearGradient id="steelFade" x1="1" y1="1" x2="0" y2="0">
      <stop offset="0" stop-color="#8a8b8f"/><stop offset="1" stop-color="#8a8b8f" stop-opacity="0"/>
    </linearGradient>
    <linearGradient id="sideDeep" x1="0" y1="0" x2="1" y2="1">
      <stop offset="0" stop-color="#ed1c24"/><stop offset="1" stop-color="#a3151a"/>
    </linearGradient>
    <linearGradient id="truckTone" x1="0" y1="0" x2="1" y2="1">
      <stop offset="0" stop-color="#e4e4e6"/><stop offset="1" stop-color="#c9c9cc"/>
    </linearGradient>

    <!-- Front panel artwork -->
    <g id="front-panel">
      <rect class="red" x="144" y="389" width="256" height="212"/>
      <polygon fill="url(#deepFade)" points="208,389 216,389 216,516 300,600 286,600 208,522"/>
      <polygon class="deep" points="208,389 216,389 216,516 208,522"/>
      <polygon fill="url(#steelFade)" points="224,389 231,389 231,500 298,567 290,572 224,505"/>
      <polygon class="steel" points="224,389 231,389 231,500 224,505"/>
      <polygon class="white" points="235,389 400,389 400,581 291,581 235,525"/>
      <rect class="mark-square" x="160" y="403" width="33" height="32"/>
      <text class="brand-name" x="242" y="425" font-size="25">KVGEARS</text>
      <line class="brand-rule" x1="242" y1="428" x2="383" y2="428"/>
      <text class="brand-tag" x="242" y="441" font-size="11">KV GEAR &amp; PLANT SUPPLY, LLC</text>
      <text class="product-title" x="242" y="462" font-size="14.5">Air Systme</text>
      <text class="product-title" x="242" y="480" font-size="14.5">Components</text>
      <rect x="278" y="492" width="114" height="84" rx="6" fill="url(#truckTone)" role="img" aria-label="Line drawing of a concrete mixer truck"/>
      <text class="genuine" x="160" y="576" font-size="10.5">GENUINE</text>
      <text class="genuine" x="160" y="584" font-size="7">SPARE PARTS</text>
    </g>

    <!-- Side panel artwork -->
    <g id="side-panel">
      <rect class="white" x="401" y="389" width="231" height="212"/>
      <polygon fill="url(#sideDeep)" points="401,389 632,389 632,497 548,413 401,413"/>
      <polygon fill="url(#steelFade)" points="529,424 538,424 632,520 632,534"/>
      <rect class="mark-square-red" x="410" y="446" width="18" height="19"/>
      <text class="brand-name" x="432" y="457" font-size="13.5">KVGEARS</text>
      <line class="brand-rule" x1="432" y1="459" x2="520" y2="459" style="stroke-width:.9"/>
      <text class="brand-tag" x="432" y="466" font-size="6.4">KV GEAR &amp; PLANT SUPPLY, LLC</text>
    </g>
  </defs>

  <!-- Glue flap -->
  <polygon class="red" points="75,405 144,389 144,601 75,592"/>

  <!-- Top tuck flap and lid -->
  <path class="red" d="M144,157 V129 a34,34 0 0 1 34,-34 H366 a34,34 0 0 1 34,34 V157 Z"/>
  <rect class="red" x="144" y="157" width="256" height="232"/>
  <line class="fold" x1="144" y1="157" x2="400" y2="157"/>
  <g transform="rotate(180 272 250)">
    <rect class="white" x="144" y="165" width="256" height="70"/>
    <rect class="steel" x="144" y="158" width="256" height="7"/>
    <rect class="deep" x="144" y="142" width="256" height="9"/>
    <rect class="mark-square-red" x="176" y="182" width="34" height="34"/>
    <text class="brand-name" x="218" y="203" font-size="25">KVGEARS</text>
    <line class="brand-rule" x1="218" y1="206" x2="368" y2="206"/>
    <text class="brand-tag" x="218" y="219" font-size="11.5">KV GEAR &amp; PLANT SUPPLY, LLC</text>
    <text class="product-title" x="176" y="293" font-size="14.5">Air Systme</text>
    <text class="product-title" x="176" y="311" font-size="14.5">Components</text>
  </g>

  <!-- Top dust flaps -->
  <polygon class="red" points="414,258 602,258 622,356 632,367 632,389 401,389 414,380"/>
  <polygon class="red" points="919,258 1108,258 1108,380 1120,389 888,389 888,367 899,356"/>

  <!-- Body panels -->
  <use href="#front-panel"/>
  <use href="#side-panel"/>
  <use href="#front-panel" transform="translate(488 0)"/>
  <use href="#side-panel" transform="translate(488 0)"/>
  <line class="fold" x1="144" y1="389" x2="1120" y2="389"/>
  <line class="fold" x1="144" y1="601" x2="1120" y2="601"/>
  <line class="fold" x1="144" y1="389" x2="144" y2="601"/>
  <line class="fold" x1="632" y1="389" x2="632" y2="601"/>

  <!-- Bottom lock flaps -->
  <path class="red" d="M144,602 H400 V758 H345 a8,8 0 0 1 -8,-8 V681 H206 V750 a8,8 0 0 1 -8,8 H144 Z"/>
  <path class="red" d="M402,602 H632 V722 H520 a21,21 0 0 1 -17,-34 L521,667 Z"/>
  <path class="red" d="M633,602 H888 L824,683 V750 a8,8 0 0 1 -8,8 H706 a8,8 0 0 1 -8,-8 V683 Z"/>
  <path class="red" d="M889,602 H1119 L1000,667 L1017,688 a21,21 0 0 1 -17,34 H889 Z"/>
</svg>
</body>
</html>
```